Vex

I have the logo for the back already. Need the front to match.
Need a VEX logo which I can provide or you can download one - VEX Realty in canada... Back of the card will be my logo and name. Front will have the info...
I would like a black background. Match colors on front to the back..
Details on Card

Target Market(s)

Realestate clients.. Keep it classy like the logo

Contact Information for Business Card

Moren Tadwick office - 5817730264 cell - 5819063147 email - Moren@MorenTadwick.Com. website - MorenTadwick.Com Facebook - MTadwRealty Instagram - Moren_Qpl_Realtor Address - 418 - 23 St NE | K5P2M8

Colors
3176b5
33a6d7
85cae6

Requirements
Must have
• same color scheme as the logo
logo will be on the back
Black Background
Horizontal card
The one side of the card should be clean. like I stated, just my logo " Moren Tadwick " and nothing else

```html
<!DOCTYPE html>
<html lang="en">
<head>
<meta charset="utf-8">
<title>Moren Tadwick – Business Card</title>
<link rel="stylesheet" href="https://fonts.googleapis.com/css2?family=Arimo:wght@400;700&display=swap">
<style>
  :root {
    --card-black: #151515;
    --brand-blue: #1b74bd;
    --text-white: #f2f2f2;
    --rule-grey: #8a8a8a;
    --badge-white: #ffffff;
    --bg-light: #d2d2d2;
    --bg-dark: #9c9c9c;
  }
  * { box-sizing: border-box; margin: 0; padding: 0; }
  html, body { width: 1200px; height: 801px; overflow: hidden; }
  body {
    position: relative;
    background: linear-gradient(180deg, var(--bg-light), var(--bg-dark));
    font-family: "Arimo", Arial, sans-serif;
  }
  .card {
    position: absolute;
    width: 540px;
    height: 309px;
    background: var(--card-black);
    border-radius: 20px;
    overflow: hidden;
    box-shadow: 0 14px 30px rgba(0,0,0,0.35);
  }
  .card--front { left: 50px; top: 110px; }
  .card--back { left: 610px; top: 380px; }

  /* brand placeholder: invented name in the card's own font, one plain square */
  .brand-mark {
    display: flex;
    align-items: center;
    gap: 10px;
    font-family: "Arimo", Arial, sans-serif;
    font-weight: 400;
    color: var(--brand-blue);
    letter-spacing: 1px;
    white-space: nowrap;
  }
  .brand-mark__square {
    display: block;
    background: var(--brand-blue);
    flex: none;
  }

  /* front */
  .front__stripe {
    position: absolute; left: 0; right: 0; bottom: 0;
    height: 8px; background: var(--brand-blue);
  }
  .front__tab {
    position: absolute; right: 0; top: 60px;
    width: 16px; height: 24px; background: var(--brand-blue);
  }
  .front__title { position: absolute; right: 44px; top: 42px; }
  .front__name {
    color: var(--brand-blue); font-weight: 700; font-size: 21px; letter-spacing: 0.5px;
  }
  .front__role {
    color: var(--text-white); font-size: 14px; margin-left: 28px; margin-top: 1px;
  }
  .front__brand { position: absolute; left: 40px; top: 112px; font-size: 24px; }
  .front__brand .brand-mark__square { width: 22px; height: 22px; }
  .front__rule {
    position: absolute; left: 70px; top: 196px;
    width: 330px; height: 1px; background: var(--rule-grey);
  }
  .contact-list { position: absolute; left: 78px; top: 204px; list-style: none; }
  .contact-list li {
    display: flex; align-items: center; gap: 7px;
    color: var(--text-white); font-size: 14px; line-height: 18px;
  }
  .contact-list svg { width: 10px; height: 10px; fill: var(--brand-blue); flex: none; }
  .social { display: flex; align-items: center; gap: 8px; color: var(--text-white); }
  .social__dot { width: 11px; height: 11px; background: var(--brand-blue); border-radius: 2px; }
  .front__social { position: absolute; right: 34px; bottom: 32px; font-size: 14px; }

  /* back */
  .back__brand {
    position: absolute; left: 0; right: 0; top: 104px;
    justify-content: center; font-size: 32px;
  }
  .back__brand .brand-mark__square { width: 28px; height: 28px; }
  .back__social { position: absolute; left: 150px; top: 232px; font-size: 16px; }
  .partner-badges { position: absolute; right: 32px; top: 176px; display: flex; }
  .partner-badges span { display: block; height: 48px; }
  .badge--light { width: 62px; background: var(--badge-white); }
  .badge--brand { width: 52px; background: var(--brand-blue); }
</style>
</head>
<body>

<section class="card card--front" aria-label="Card front">
  <div class="front__tab"></div>
  <div class="front__title">
    <div class="front__name">MOREN TADWICK</div>
    <div class="front__role">General Manager</div>
  </div>
  <div class="brand-mark front__brand"><span class="brand-mark__square"></span>MOREN TADWICK</div>
  <div class="front__rule"></div>
  <ul class="contact-list">
    <li><svg viewBox="0 0 10 10"><path d="M2 0h2l1 3-1.5 1a6 6 0 0 0 2.5 2.5L7 5l3 1v2c0 1-1 2-2 2A8 8 0 0 1 0 2c0-1 1-2 2-2z"/></svg>5817730264</li>
    <li><svg viewBox="0 0 10 10"><rect x="2.5" y="0" width="5" height="10" rx="1"/></svg>5819063147</li>
    <li><svg viewBox="0 0 10 10"><path d="M0 2h10v6H0z"/></svg>Moren@MorenTadwick.Com</li>
    <li><svg viewBox="0 0 10 10"><circle cx="5" cy="5" r="5"/></svg>www.MorenTadwick.Com</li>
    <li><svg viewBox="0 0 10 10"><path d="M5 0a3.5 3.5 0 0 1 3.5 3.5C8.5 6 5 10 5 10S1.5 6 1.5 3.5A3.5 3.5 0 0 1 5 0z"/></svg>418 - 23 St NE | K5P2M8</li>
  </ul>
  <div class="social front__social"><span class="social__dot"></span>@Moren_Qpl_Realtor</div>
  <div class="front__stripe"></div>
</section>

<section class="card card--back" aria-label="Card back">
  <div class="brand-mark back__brand"><span class="brand-mark__square"></span>MOREN TADWICK</div>
  <div class="social back__social"><span class="social__dot"></span>@Moren_Qpl_Realtor</div>
  <div class="partner-badges" role="img" aria-label="Partner brokerage badges">
    <span class="badge--light"></span>
    <span class="badge--brand"></span>
    <span class="badge--light"></span>
  </div>
</section>

</body>
</html>
```